Brochure Design Project

We are a consulting engineering company and need to have our current company brochure updated and made to look a lot more professional.

We provide design and documentation of electrical, lighting, mechanical, hydraulic, fire, services to architects, interior designers, building owners and managers.

We are launching an updated website shortly and want a print brochure to send to clients.

Attached is our current brochure for reference.
Updates

The recent projects section should be renamed to "Completed Projects". Space should be allowed for 8 projects. I have uploaded 7 of these images and a new image will follow shortly.

We would like to include an image for each of our company services. I have uploaded 9 new images:

1. Electrical
2. Mechanical
3. Communications
4. Fire
5. Security
6. Lighting
7. Hydraulics
8. Computer Suite
9. Building Assessments

Target Market(s)

Architects, Interior Designers, Consultants, Professionals

Industry/Entity Type

Building

Requirements
Must have
• Very professional look
Simple and easy to read layout
Similar look and feel to our new website which is soon to be launched : http://www.sitehaven.co.uk/rkm/
Examples of our recent projects - around 6 projects with 1 or 2 photos per project. Will upload these soon.
A3 size, double sided with centre fold
Should not have
• Bright colours
Any comics or similar

```html
<!DOCTYPE html>
<html lang="en">
<head>
<meta charset="utf-8">
<title>Services Spread</title>
<link rel="stylesheet" href="https://fonts.googleapis.com/css2?family=PT+Sans&display=swap">
<style>
  :root {
    --page: #e9eaeb;
    --page-light: #f4f4f4;
    --band-dark: #1f1f1f;
    --bar-dark: #232323;
    --head-light: #d9dbdc;
    --head-mid: #a9acae;
    --ink: #222222;
    --mark: #8a8a8a;
  }
  * { box-sizing: border-box; margin: 0; padding: 0; }
  html, body { width: 1200px; height: 849px; overflow: hidden; }
  body {
    position: relative;
    font-family: "PT Sans", Arial, sans-serif;
    background: radial-gradient(ellipse at 50% 45%, var(--page-light) 0%, var(--page) 70%, #dcdddf 100%);
    color: var(--ink);
  }
  .top-band {
    position: absolute; left: 0; top: 0; width: 1200px; height: 50px;
    background: linear-gradient(90deg, var(--head-mid) 0%, var(--head-light) 40%, #e4e5e6 55%, var(--head-mid) 100%);
  }
  .top-rule {
    position: absolute; left: 0; top: 50px; width: 1200px; height: 18px;
    background: linear-gradient(90deg, #2a2a2a 0%, #3a3a3a 50%, #2a2a2a 100%);
  }
  .bottom-band {
    position: absolute; left: 0; top: 768px; width: 1200px; height: 81px;
    background: var(--band-dark);
  }
  .bar { position: absolute; width: 14px; background: var(--bar-dark); }
  .bar-left-top { left: 46px; top: 68px; height: 344px; }
  .bar-left-bottom { left: 536px; top: 420px; height: 348px; }
  .bar-right-top { left: 648px; top: 68px; height: 344px; }
  .bar-right-bottom { left: 1140px; top: 420px; height: 348px; }

  .photo {
    position: absolute; width: 213px; height: 141px; border-radius: 7px;
    box-shadow: 0 3px 6px rgba(0,0,0,0.35), 0 0 0 1px rgba(255,255,255,0.6);
  }
  .photo-office { left: 288px; top: 121px; background: linear-gradient(160deg, #f2f2f0 0%, #d9d8d2 55%, #6e6d68 100%); }
  .photo-reception { left: 78px; top: 359px; background: linear-gradient(180deg, #2a2a2c 0%, #7e858b 40%, #c9c9c7 70%, #9d9b98 100%); }
  .photo-meeting { left: 288px; top: 567px; background: linear-gradient(170deg, #f1efea 0%, #dcd8d0 55%, #55534f 100%); }
  .photo-site { left: 689px; top: 120px; background: linear-gradient(180deg, #4a78b3 0%, #dfe6ee 45%, #8b8680 65%, #b7aa98 100%); }
  .photo-tower { left: 898px; top: 358px; background: linear-gradient(200deg, #bfd5ee 0%, #6c95c8 40%, #1f4f99 75%, #163a78 100%); }
  .photo-city { left: 689px; top: 567px; background: linear-gradient(180deg, #6d8fb6 0%, #a9c2d6 40%, #c2ab86 70%, #4d4439 100%); }

  .service { position: absolute; list-style: none; font-size: 11.5px; line-height: 14px; }
  .service li { display: block; }
  .svc-electrical-a { left: 79px; top: 86px; width: 206px; }
  .svc-electrical-b { left: 309px; top: 331px; width: 212px; }
  .svc-computer { left: 79px; top: 564px; width: 205px; }
  .svc-hydraulic { left: 79px; top: 638px; width: 205px; }
  .svc-communication { left: 920px; top: 80px; width: 190px; }
  .svc-security { left: 920px; top: 243px; width: 190px; }
  .svc-fire { left: 690px; top: 304px; width: 190px; }
  .svc-building { left: 691px; top: 402px; width: 200px; }
  .svc-mechanical { left: 920px; top: 559px; width: 192px; }

  .brand {
    position: absolute; top: 786px;
    font-size: 38px; line-height: 44px; color: var(--mark); letter-spacing: 1px;
  }
  .brand-left { left: 33px; }
  .brand-right { left: 1100px; }
</style>
</head>
<body>
  <div class="top-band"></div>
  <div class="top-rule"></div>
  <div class="bar bar-left-top"></div>
  <div class="bar bar-left-bottom"></div>
  <div class="bar bar-right-top"></div>
  <div class="bar bar-right-bottom"></div>

  <div class="photo photo-office" role="img" aria-label="Open-plan office with workstations and linear ceiling lighting"></div>
  <div class="photo photo-reception" role="img" aria-label="Modern reception area with black ceiling and feature staircase"></div>
  <div class="photo photo-meeting" role="img" aria-label="Meeting room with table, chairs and projection screen"></div>
  <div class="photo photo-site" role="img" aria-label="Building construction site under a cloudy blue sky"></div>
  <div class="photo photo-tower" role="img" aria-label="Blue glass office tower against the sky"></div>
  <div class="photo photo-city" role="img" aria-label="City street with glass towers and heritage buildings"></div>

  <ul class="service svc-electrical-a">
    <li>Electrical Services</li>
    <li>Power distribution</li>
    <li>General lighting</li>
    <li>Feature lighting for highlight/contrast of client orientated areas</li>
    <li>Programmable lighting control</li>
    <li>Emergency lighting and exit signs</li>
    <li>Electrical consumption management</li>
    <li>Lighting control integration with energy management systems</li>
    <li>Evacuation warning systems</li>
    <li>Power conditioners</li>
    <li>Public address installations</li>
    <li>Television signal distribution</li>
  </ul>

  <ul class="service svc-electrical-b">
    <li>Electrical Services</li>
    <li>Power distribution</li>
    <li>General lighting</li>
    <li>Feature lighting for highlight/contrast of client orientated areas</li>
    <li>Programmable lighting control</li>
    <li>Emergency lighting and exit signs</li>
    <li>Electrical consumption management</li>
    <li>Lighting control integration with energy management systems</li>
    <li>Evacuation warning systems</li>
    <li>Power conditioners</li>
    <li>Public address installations</li>
    <li>Television signal distribution</li>
  </ul>

  <ul class="service svc-computer">
    <li>Computer Suite Audits</li>
    <li>Comprehensive Computer Suite Audits</li>
    <li>Australian Standard Compliance</li>
    <li>TIA 942 Tier Rating certification</li>
  </ul>

  <ul class="service svc-hydraulic">
    <li>Hydraulic Services</li>
    <li>Water supplies</li>
    <li>Waste discharge</li>
    <li>Venting</li>
    <li>Water heating and cooling</li>
    <li>Filtration</li>
  </ul>

  <ul class="service svc-communication">
    <li>Communication Systems</li>
    <li>Telephone cabling</li>
    <li>Data cabling</li>
    <li>Patching philosophies</li>
    <li>Fibre optic distribution systems</li>
    <li>Integration of voice and<br>data cabling systems</li>
    <li>Hardware housings</li>
    <li>Compliance with relevant codes and installation practices</li>
    <li>LAN Cable distribution systems</li>
  </ul>

  <ul class="service svc-security">
    <li>Security Services</li>
    <li>Electronic access control</li>
    <li>Integration of existing systems with client requirements</li>
    <li>Intruder detection</li>
    <li>Off site monitoring and alarms</li>
    <li>CCTV</li>
  </ul>

  <ul class="service svc-fire">
    <li>Fire Services</li>
    <li>Electronic Smoke and Thermal Detec&shy;tion</li>
    <li>AERIS Systems</li>
    <li>Fire Suppression Systems</li>
    <li>Fire Sprinkler Systems</li>
  </ul>

  <ul class="service svc-building">
    <li>Building Assessment</li>
    <li>Building services condition assessment</li>
    <li>Advise relative to available building ser&shy;vices (for long or short term purpose)</li>
    <li>Trouble Shooting and Investigation</li>
    <li>Review of Existing Systems</li>
    <li>Upgrade for Current and Future Refur&shy;bishment</li>
  </ul>

  <ul class="service svc-mechanical">
    <li>Mechanical Services</li>
    <li>District Cooling System</li>
    <li>Air and Water Cooled Chilled Water System</li>
    <li>BMS/BAS and DDC Control System</li>
    <li>Computer and Data Centre Solutions</li>
    <li>DX-Type Water and Air<br>Cooled System (Single or<br>Multiple Indoor Units)</li>
    <li>VAV and Chilled Beams</li>
    <li>Industrial and Commercial<br>Humidification</li>
    <li>Commercial and Industrial Evaporative Cooling Using Air Washers</li>
  </ul>

  <div class="bottom-band"></div>
  <div class="brand brand-left">rkm</div>
  <div class="brand brand-right">rkm</div>
</body>
</html>
```